Attention grabbing 6x9 postcard

We are looking to have an attention grabbing post card that be sent out to homeowners from our roofing company Olum Roofing. the concept is that on the front it will say something like (STOP THE KNOCKING!
Tired of roofers knocking on your door? Contact us because we value your time as much as you value the roof over your head."
Olum Roofing
OlumRoofing.com
877.612.OLUM
info@olumroofing.com

Please feel free to come up with something very creative. Once we pick the final design we will provide the copy.

```html
<!DOCTYPE html>
<html lang="en">
<head>
<meta charset="utf-8">
<title>Olum Roofing Postcard</title>
<link rel="stylesheet" href="https://fonts.googleapis.com/css2?family=Oswald:wght@500;600&family=Poppins:wght@600&display=swap">
<style>
:root{
  --honey:#E8B84A;
  --honey-deep:#D9A631;
  --ink:#111111;
  --charcoal:#2E2F31;
  --white:#FFFFFF;
  --page:#E9EAEB;
}
*{margin:0;padding:0;box-sizing:border-box}
html,body{width:1200px;height:1200px;overflow:hidden;background:var(--page)}
.canvas{position:relative;width:1200px;height:1200px}
.card{position:absolute;overflow:hidden}

/* Front */
.front{left:265px;top:180px;width:585px;height:389px;
  background:linear-gradient(160deg,#EDC25A 0%,var(--honey) 55%,#D3A947 100%)}
.front-photo{position:absolute;left:0;top:226px;width:585px;height:119px;
  background:linear-gradient(100deg,#3A3B3D 0%,#2A2B2D 60%,#45464A 100%)}
.front-title{position:absolute;left:27px;top:22px;font-family:'Oswald',sans-serif;font-weight:600;
  font-size:52px;line-height:56px;color:var(--white);letter-spacing:.5px}
.logo-box{position:absolute;left:257px;top:0;width:140px;height:79px;background:var(--white);
  display:flex;align-items:center;justify-content:center}
.logo-name{font-family:'Oswald',sans-serif;font-weight:500;font-size:14px;letter-spacing:1.5px;color:var(--honey)}
.hex-art{position:absolute;left:0;top:0}
.headline-band{position:absolute;left:0;top:158px;width:370px;height:68px;background:var(--white);
  display:flex;align-items:center;padding-left:30px}
.headline{font-family:'Oswald',sans-serif;font-weight:600;font-size:33px;color:var(--ink)}
.pitch{position:absolute;left:30px;top:236px;font-family:'Poppins',sans-serif;font-weight:600;
  font-size:16px;line-height:24px;color:var(--honey);white-space:nowrap}
.front-footer{position:absolute;left:0;top:345px;width:585px;height:44px;background:var(--honey);
  display:flex;align-items:center;gap:20px;padding-left:28px}
.contact{display:flex;align-items:center;gap:8px;font-family:'Oswald',sans-serif;font-weight:500;
  font-size:14px;color:var(--ink)}
.contact svg{width:16px;height:16px;flex:none}
.front .hex-small{position:absolute;left:0;top:0}

/* Back */
.back{left:345px;top:669px;width:595px;height:375px;background:var(--white)}
.back-shape{position:absolute;left:0;top:0}
.back-title{position:absolute;left:42px;top:10px;font-family:'Oswald',sans-serif;font-weight:600;
  font-size:40px;line-height:42px;color:var(--honey)}
.back-contacts{position:absolute;left:42px;top:104px;display:flex;flex-direction:column;gap:11px}
.back-contacts .contact{color:var(--white);font-size:16px;gap:10px}
.back-contacts .contact svg{width:20px;height:20px}
.photo-frame{position:absolute;top:16px;width:144px;height:115px;background:var(--white);padding:5px}
.photo-frame .fill{width:100%;height:100%}
.frame-one{left:260px}
.frame-two{left:419px}
.stamp-box{position:absolute;left:46px;top:241px;width:113px;height:104px;border:1.5px solid var(--honey-deep)}
.address-line{position:absolute;left:277px;width:275px;height:1.5px;background:var(--honey-deep)}
.back-footer{position:absolute;left:0;top:362px;width:595px;height:13px;background:var(--honey)}
</style>
</head>
<body>
<div class="canvas">

  <section class="card front">
    <div class="front-photo" role="img" aria-label="Dark shingled roof photograph"></div>
    <h1 class="front-title">OLUM<br>ROOFING</h1>
    <div class="logo-box"><span class="logo-name">OLUM ROOFING</span></div>

    <svg class="hex-art" width="585" height="389" viewBox="0 0 585 389" role="img" aria-label="Photograph of a hand knocking on a front door">
      <defs>
        <linearGradient id="doorTone" x1="0" y1="0" x2="1" y2="0">
          <stop offset="0" stop-color="#2A2B2D"/><stop offset=".6" stop-color="#35363A"/><stop offset="1" stop-color="#4C6F9E"/>
        </linearGradient>
      </defs>
      <polygon points="366,129 436,8 576,8 646,129 576,250 436,250" fill="var(--white)"/>
      <polygon points="378,129 442,18 570,18 634,129 570,240 442,240" fill="var(--honey)"/>
      <polygon points="390,129 448,28 564,28 622,129 564,230 448,230" fill="url(#doorTone)"/>
    </svg>

    <div class="headline-band"><h2 class="headline">STOP THE KNOCKING!</h2></div>
    <p class="pitch">Tired of roofers knocking on your<br>door? Contact us because we value<br>your time as much as you value the<br>roof over your head."</p>

    <footer class="front-footer">
      <span class="contact"><svg viewBox="0 0 20 20"><circle cx="10" cy="10" r="10" fill="var(--ink)"/><path d="M7 5.5l1.6 2.2-1 1.2a6 6 0 0 0 3.5 3.5l1.2-1 2.2 1.6-.8 1.7C9 14.5 5.5 11 5.3 6.3z" fill="var(--honey)"/></svg>877.612.OLUM</span>
      <span class="contact"><svg viewBox="0 0 20 20"><circle cx="10" cy="10" r="10" fill="var(--ink)"/><rect x="5" y="6.5" width="10" height="7" fill="var(--honey)"/><path d="M5 6.5l5 4 5-4" fill="none" stroke="var(--ink)" stroke-width="1.2"/></svg>INFO@OLUMROOFING.COM</span>
      <span class="contact"><svg viewBox="0 0 20 20"><circle cx="10" cy="10" r="10" fill="var(--ink)"/><g fill="none" stroke="var(--honey)" stroke-width="1.2"><circle cx="10" cy="10" r="5.5"/><ellipse cx="10" cy="10" rx="2.3" ry="5.5"/><path d="M4.5 10h11"/></g></svg>OLUMROOFING.COM</span>
    </footer>

    <svg class="hex-small" width="585" height="389" viewBox="0 0 585 389" role="img" aria-label="Photograph of a house dormer with grey shingles">
      <defs>
        <linearGradient id="roofTone" x1="0" y1="0" x2="0" y2="1">
          <stop offset="0" stop-color="#C9DCEB"/><stop offset=".55" stop-color="#7E8894"/><stop offset="1" stop-color="#4A4E55"/>
        </linearGradient>
      </defs>
      <polygon points="447,285 496,200 594,200 643,285 594,370 496,370" fill="var(--white)"/>
      <polygon points="461,285 503,212 587,212 629,285 587,358 503,358" fill="var(--honey)"/>
      <polygon points="473,285 509,223 581,223 617,285 581,347 509,347" fill="url(#roofTone)"/>
    </svg>
  </section>

  <section class="card back">
    <svg class="back-shape" width="595" height="375" viewBox="0 0 595 375">
      <polygon points="0,0 582,0 582,163 267,163 160,216 0,216" fill="var(--ink)"/>
      <polyline points="160,219 267,166 582,166" fill="none" stroke="var(--honey)" stroke-width="2"/>
      <rect x="582" y="0" width="13" height="320" fill="var(--honey)"/>
    </svg>
    <h1 class="back-title">OLUM<br>ROOFING</h1>
    <div class="back-contacts">
      <span class="contact"><svg viewBox="0 0 20 20"><circle cx="10" cy="10" r="10" fill="var(--honey)"/><path d="M7 5.5l1.6 2.2-1 1.2a6 6 0 0 0 3.5 3.5l1.2-1 2.2 1.6-.8 1.7C9 14.5 5.5 11 5.3 6.3z" fill="var(--ink)"/></svg>877.612.OLUM</span>
      <span class="contact"><svg viewBox="0 0 20 20"><circle cx="10" cy="10" r="10" fill="var(--honey)"/><rect x="5" y="6.5" width="10" height="7" fill="var(--ink)"/><path d="M5 6.5l5 4 5-4" fill="none" stroke="var(--honey)" stroke-width="1.2"/></svg>INFO@OLUMROOFING.COM</span>
      <span class="contact"><svg viewBox="0 0 20 20"><circle cx="10" cy="10" r="10" fill="var(--honey)"/><g fill="none" stroke="var(--ink)" stroke-width="1.2"><circle cx="10" cy="10" r="5.5"/><ellipse cx="10" cy="10" rx="2.3" ry="5.5"/><path d="M4.5 10h11"/></g></svg>OLUMROOFING.COM</span>
    </div>
    <div class="photo-frame frame-one"><div class="fill" role="img" aria-label="House gable with dormer window and grey shingles" style="background:linear-gradient(180deg,#C7D6E3 0%,#8E949C 45%,#4F545B 100%)"></div></div>
    <div class="photo-frame frame-two"><div class="fill" role="img" aria-label="Green metal roof with white gable trim against blue sky" style="background:linear-gradient(180deg,#9CC0DE 0%,#B9CCD8 40%,#5E7168 100%)"></div></div>
    <div class="stamp-box"></div>
    <div class="address-line" style="top:221px"></div>
    <div class="address-line" style="top:281px"></div>
    <div class="address-line" style="top:340px"></div>
    <div class="back-footer"></div>
  </section>

</div>
</body>
</html>
```